Exhibition Stand Design for innovative Social Business

We are an innovative social business empowering people to value nature through ZUN, a complementary digital currency. We have attached the TEK_ZUN branding document, and are needing a design for our exhibition stand (https://fairbuildlab.com/produit/stand-parapluie-classic-pvc-3x4c/. The attached doc mocks up a stand on page 32, though we would like some messaging included, in line with our website www.tekzun.ch. You will see there how the branding concept has been implemented with the TEK:GROW, SHARE, THRIVE wording, as well as Everyone wins. Our green colours are included in the branding document. Many thanks!

Industry/Entity Type

Environment

Font styles to use
Other font styles liked:
• As per our attached fonts

Requirements
Must have
• Our attached branding guidelines gives our look and feel - Innovative / Dynamic / Vibrant / Reliable / Accessible / Connected.

```html
<!DOCTYPE html>
<html lang="en">
<head>
<meta charset="utf-8">
<title>TEK ZUN Exhibition Backwall</title>
<link rel="stylesheet" href="https://fonts.googleapis.com/css2?family=Lexend:wght@600;700&family=Quicksand:wght@700&display=swap">
<style>
  :root {
    --bg: #e9e9e9;
    --panel: #f1f1f1;
    --ink: #121212;
    --green: #25e23f;
    --mint: #4fdca6;
    --aqua: #86e3cd;
  }
  * { margin: 0; padding: 0; box-sizing: border-box; }
  html, body {
    width: 1200px;
    height: 960px;
    overflow: hidden;
    background: var(--bg);
  }
  .canvas {
    position: relative;
    width: 1200px;
    height: 960px;
  }
  .backwall {
    position: absolute;
    left: 60px;
    top: 105px;
    width: 1080px;
    height: 750px;
    background: var(--panel);
    overflow: hidden;
    box-shadow: 0 10px 30px rgba(0,0,0,0.12);
  }
  .accent-top {
    position: absolute;
    left: 640px;
    top: 0;
    width: 440px;
    height: 280px;
    background: linear-gradient(90deg, #2ee84a, #55dc8a 60%, var(--aqua));
  }
  .accent-base {
    position: absolute;
    left: 0;
    top: 500px;
    width: 1080px;
    height: 250px;
    background: linear-gradient(90deg, var(--mint), #58e698 50%, var(--green));
  }
  .brand-name {
    position: absolute;
    left: 112px;
    top: 62px;
    font-family: "Lexend", sans-serif;
    font-weight: 700;
    font-size: 96px;
    line-height: 1;
    letter-spacing: -1px;
    color: var(--ink);
    white-space: nowrap;
  }
  .pillars {
    position: absolute;
    left: 112px;
    top: 190px;
    list-style: none;
    font-family: "Lexend", sans-serif;
    font-weight: 600;
    font-size: 48px;
    line-height: 68px;
    color: var(--ink);
  }
  .tagline {
    position: absolute;
    left: 560px;
    top: 318px;
    font-family: "Quicksand", sans-serif;
    font-weight: 700;
    font-size: 54px;
    line-height: 1.2;
    background: linear-gradient(90deg, var(--mint), var(--green));
    -webkit-background-clip: text;
    background-clip: text;
    color: transparent;
    white-space: nowrap;
  }
  .website {
    position: absolute;
    left: 660px;
    top: 625px;
    font-family: "Quicksand", sans-serif;
    font-weight: 700;
    font-size: 44px;
    line-height: 1.2;
    color: var(--ink);
    white-space: nowrap;
  }
</style>
</head>
<body>
<main class="canvas">
  <section class="backwall" aria-label="TEK ZUN exhibition backwall">
    <div class="accent-top" role="img" aria-label="Decorative green gradient shape"></div>
    <div class="accent-base" role="img" aria-label="Decorative green gradient wave band"></div>
    <p class="brand-name">TEK ZUN</p>
    <ul class="pillars">
      <li>TEK:</li>
      <li>GROW</li>
      <li>SHARE</li>
      <li>THRIVE</li>
    </ul>
    <p class="tagline">everyone wins</p>
    <p class="website">www.tekzun.ch</p>
  </section>
</main>
</body>
</html>
```